Need a high-impact website built for used car dealership

I am seeking a high impact website built on Pagecraft for my used car dealership.

The name of the dealership is Motor Harbor Depot, Inc. A copy of our logo is attached. Our company colors are blue and orange and should be incorporated into the website.

The overall look and feel of the website should be clean, easy to navigate, classy yet contemporary. Customers should be able to navigate the site quickly without it being cumbersome.The site should look custom built and NOT like a generic template.

Here are some details that must be incorporated into the final product:
** The site should be highly optimized for white hat SEO (headlines, content, page structure; keyword use, title tags, meta descriptions, clean index, fast page loads, etc)
** Site must be fully mobile responsive
** Site should be setup for Trackwell Metrics and Friendloop Beacon tracking
** Site must include live chat functionality; if no one is available to respond to the live chat the system should send an email with the consumers information.
** Include a "like" button that allows customers to like/follow our Friendloop page from the website
** Include exit prompt/popup to collect email address and phone number
** Include a finance app (example: https://www.harlowmotorgroup.example/FinancePreQualForm)
** Include a reviews function similiar to the one on brookfields page: https://www.brookfield-autos.example/write-review-select-rating/
If customer selects 1, 2, or 3 star rating they post a review that is sent to us via email; If customer selects 4 or 5 star rating it posts a Trackwell or Ratebox review which becomes visible on the site
** Include ability to email or text message a link to a specific vehicle
** Include ability for customer to share a vehicle on Friendloop
** Include ability for user to mark specific vehicles "favorites" so they can easily view them again
** Include ability to filter vehicles by year, make, model, mileage, color and drivetrain or any combination of those when searching inventory
** include paysecure.example credit card payments.
** Customer must be able to call our dealership on a mobile device by clicking on the phone number on the main page
**Customer must be able to click on our address on the main page and have it link to their native maps app on their mobile device
** Vehicle inventory will import from our AutoListHub.example account. The listing data will be provided in a CSV or TXT file, which will include links to the photographs of the vehicles.
** Include logos of all the major car manufacturers on the home page: Velor, Zent, KRV, Tovan, Marivel, Dunharrow, Pelgrave, Brant, Holm, VTR, Kespa, Oravik, Solvane, Pelican, Wolk, Ruv, Moor Tracker, Quarn, Bexford, Tulio, Avalina Strade, Pip, Orvel, Falkner, Tor, Hale-Winton, Vido, Plume, Kiyoto, Voltra, Harumi, Strassfahr, and Norda.

Attached is one example I like. I’d like to see a design like this as well as your own creative work.

• See above
• Site must have a clean, custom look that does not appear to be a cookie-cutter website

```html
<!DOCTYPE html>
<html lang="en">
<head>
<meta charset="utf-8">
<title>Motor Harbor Depot — Quality Used Cars</title>
<link href="https://fonts.googleapis.com/css2?family=Roboto:wght@400;500;700&family=Poppins:wght@600;700&display=swap" rel="stylesheet">
<style>
:root{
  --blue:#0a82c9;
  --blue-dark:#066aa6;
  --black:#000;
  --ink:#1b1b1b;
  --muted:#666;
  --line:#d8d8d8;
  --band:#e5e6e8;
  --footer:#2a2a2a;
  --star:#f5a623;
  --white:#fff;
}
*{box-sizing:border-box;margin:0;padding:0}
html,body{width:1200px;height:2912px;overflow:hidden}
body{font-family:Roboto,Arial,sans-serif;color:var(--ink);background:var(--white);position:relative}
.abs{position:absolute}
svg{display:block}

/* Header */
.site-header{position:absolute;left:0;top:0;width:1200px;height:120px;background:var(--black);color:var(--white)}
.brand{left:111px;top:30px;font-family:Roboto,sans-serif;font-weight:700;font-size:25px;color:var(--white);line-height:30px;width:190px}
.top-fav{left:410px;top:18px;display:flex;align-items:center;gap:8px;font-size:15px}
.top-circle{width:40px;height:40px;border-radius:50%;background:var(--white);display:flex;align-items:center;justify-content:center}
.top-mail{left:506px;top:6px;display:flex;align-items:center;gap:24px;font-size:15px}
.top-phone{left:815px;top:6px;display:flex;align-items:center;gap:24px;font-size:30px;font-weight:500}
.main-nav{left:380px;top:78px;display:flex;gap:47px;font-size:16px;font-weight:700}
.main-nav a{color:var(--white);text-decoration:none;position:relative;padding-bottom:12px}
.main-nav a.active{color:var(--blue)}
.main-nav a.active::after{content:"";position:absolute;left:0;right:0;bottom:0;height:3px;background:var(--blue)}
.btn{display:inline-flex;align-items:center;gap:10px;background:var(--blue);color:var(--white);font-weight:700;font-size:16px;text-decoration:none}
.sign-in{left:976px;top:59px;width:113px;height:50px;justify-content:center}

/* Hero */
.hero{left:0;top:120px;width:1200px;height:478px;background:linear-gradient(100deg,#3b4a3a 0%,#5d6d55 30%,#6b7568 55%,#4e5a52 75%,#39423e 100%)}
.hero-car{left:0;top:120px;width:640px;height:420px;background:radial-gradient(ellipse at 45% 55%,#c21a24 0%,#9a1119 45%,rgba(80,20,20,0) 75%)}
.hero-copy{left:628px;top:305px;color:var(--white);width:470px}
.hero-copy h1{font-size:46px;font-weight:700;letter-spacing:.5px;line-height:56px;white-space:nowrap}
.hero-copy p{font-size:16px;line-height:26px;margin-top:16px}
.hero-copy .btn{height:50px;padding:0 14px;margin-top:18px}
.dots{left:629px;top:558px;display:flex;gap:8px}
.dots span{width:13px;height:13px;border-radius:50%;background:var(--white)}
.dots span.on{background:transparent;border:2px solid var(--white)}
.side-tools{left:1163px;top:265px;display:flex;flex-direction:column;gap:6px}
.side-tools span{width:37px;height:37px;background:var(--white);display:flex;align-items:center;justify-content:center}

/* Search */
.search-band{left:0;top:598px;width:1200px;height:123px;background:linear-gradient(90deg,#0d4f85,#1b6aa6 40%,#2876b0 70%,#1a5d95)}
.search-form{left:94px;top:635px;display:flex;gap:8px}
.select{height:50px;background:var(--white);display:flex;align-items:center;justify-content:space-between;padding:0 12px;font-size:18px;color:#444}
.search-btn{width:146px;height:50px;justify-content:center;font-size:18px;margin-left:2px}

/* Makes */
.makes{left:0;top:721px;width:1200px;height:69px;background:var(--band)}
.makes-list{left:120px;top:742px;display:flex;gap:24px;font-size:14px;font-weight:500;color:#777;letter-spacing:.5px}
.makes-more{left:1040px;top:738px;width:37px;height:34px;background:var(--white);border:1px solid #bbb;display:flex;align-items:center;justify-content:center}

/* Tabs */
.tabs{left:111px;top:830px;width:978px;height:33px;border-bottom:1px solid #cfcfcf;display:flex;gap:48px;font-size:21px;font-weight:700}
.tabs span{position:relative}
.tabs span.active{color:var(--blue)}
.tabs span.active::after{content:"";position:absolute;left:0;right:0;top:30px;height:4px;background:var(--blue)}

/* Cards */
.grid{left:111px;top:893px;width:978px;display:grid;grid-template-columns:repeat(3,316px);column-gap:15px;row-gap:15px}
.card{height:390px;background:var(--white);box-shadow:0 1px 6px rgba(0,0,0,.18);padding:3px;text-align:center;position:relative}
.card .photo{height:197px}
.badge{position:absolute;left:25px;top:35px;background:var(--white);color:var(--blue);font-weight:700;font-size:17px;padding:11px 9px;border-radius:3px}
.card h3{font-size:17px;font-weight:700;line-height:26px;margin-top:15px;padding:0 20px;text-transform:uppercase}
.price{color:var(--blue);font-size:30px;font-weight:700;margin-top:10px}
.meta{display:flex;justify-content:center;gap:36px;font-size:14px;color:#555;margin-top:10px}
.meta span,.tel{display:flex;align-items:center;gap:9px}
.tel{justify-content:center;font-size:14px;color:#555;margin-top:13px}
.card.featured{background:var(--blue);color:var(--white)}
.card.featured .price,.card.featured .meta,.card.featured .tel{color:var(--white)}
.p1{background:linear-gradient(135deg,#c9c3b8,#6a5146 50%,#d4b08b)}
.p2{background:linear-gradient(135deg,#8fa9a0,#c51f2b 50%,#8a8a8a)}
.p3{background:linear-gradient(135deg,#7e6a5a,#3b8fd0 55%,#a1a8ac)}
.p4{background:linear-gradient(135deg,#3d5a2a,#e8b40c 50%,#48623a)}
.p5{background:linear-gradient(135deg,#8ab9de,#cc1e2a 55%,#e9e6df)}
.p6{background:linear-gradient(135deg,#5a5a5a,#b9b9b9 50%,#6a6a6a)}

/* Why */
.why{left:0;top:1754px;width:1200px;height:396px;background:linear-gradient(90deg,#ecedf0,#e3e6ea 55%,#f0ece8)}
.why-copy{left:111px;top:1815px;width:460px}
.why-copy h2{font-family:Poppins,sans-serif;font-size:37px;font-weight:700;letter-spacing:-.5px}
.why-copy p{font-size:16.5px;line-height:26px;color:#666;margin-top:14px;text-align:justify}
.why-copy .btn{height:50px;padding:0 9px;margin-top:20px;font-size:17px}
.why-car{left:670px;top:1815px;width:505px;height:290px;border-radius:45% 45% 20% 20%;background:radial-gradient(ellipse at 50% 55%,#d9d6cf 0%,#b8b4ab 45%,rgba(200,200,200,0) 72%)}

/* Reviews */
.reviews-title{left:0;top:2188px;width:1200px;text-align:center;font-family:Poppins,sans-serif;font-size:42px;font-weight:700}
.review{top:2278px;width:480px;height:206px;background:var(--white);box-shadow:0 1px 7px rgba(0,0,0,.2)}
.avatar{position:absolute;left:14px;top:30px;width:130px;height:130px;border-radius:50%;border:3px solid #e2e2e2;background:linear-gradient(160deg,#c8d4de,#8fa0ae)}
.quote{position:absolute;left:62px;top:139px;width:36px;height:36px;border-radius:50%;background:var(--white);box-shadow:0 1px 4px rgba(0,0,0,.25);color:var(--blue);font-weight:700;font-size:22px;display:flex;align-items:center;justify-content:center}
.review .body{position:absolute;left:183px;top:48px;width:285px}
.stars{display:flex;gap:5px}
.review p{font-size:15.5px;line-height:26px;color:#777;margin-top:12px}
.review .who{font-size:16.5px;color:#555;margin-top:10px}
.review .who b{color:var(--ink)}
.arrow{top:2361px;width:40px;height:40px;border-radius:50%;border:1px solid #bbb;display:flex;align-items:center;justify-content:center;background:var(--white)}

/* Footer */
.site-footer{left:0;top:2535px;width:1200px;height:377px;background:var(--footer);color:var(--white)}
.fcol{top:2596px}
.fcol h4{font-size:18px;font-weight:700;text-decoration:underline;text-underline-offset:4px;margin-bottom:14px}
.fcol ul{list-style:none;font-size:15.5px}
.fcol li{height:34px;display:flex;gap:14px;align-items:flex-start}
.contact-row{display:flex;gap:14px;align-items:flex-start;font-size:14px;line-height:21px;margin-bottom:18px}
.ci{width:32px;height:32px;border-radius:50%;background:var(--white);flex:none;display:flex;align-items:center;justify-content:center}
.fcol.news p{font-size:16px;line-height:26px;width:272px}
.email-field{width:272px;height:48px;background:var(--white);margin-top:14px;display:flex;align-items:center;gap:8px;padding-left:20px;color:var(--blue);font-size:14px}
.fcol .btn{height:50px;padding:0 14px;margin-top:10px}
.footer-rule{left:111px;top:2840px;width:978px;height:1px;background:#666}
.copyright{left:111px;top:2856px;font-size:15px}
.pay-name{left:950px;top:2848px;font-size:21px;font-weight:500;color:#2f7fb8}
.pay-cards{left:968px;top:2878px;display:flex;gap:4px}
.pay-cards span{width:24px;height:15px;background:#ccc;border-radius:2px}
.live-chat{left:1122px;top:2637px;width:50px;height:148px;background:var(--blue);border:2px solid #fff;border-radius:4px;display:flex;align-items:center;justify-content:center}
.live-chat span{writing-mode:vertical-rl;font-weight:700;font-size:16px;letter-spacing:.5px}
</style>
</head>
<body>

<header class="site-header">
  <div class="abs brand">Motor Harbor Depot</div>
  <div class="abs top-fav">
    <svg width="16" height="14" viewBox="0 0 16 14"><path d="M8 14 1.3 7.2A4 4 0 0 1 8 2a4 4 0 0 1 6.7 5.2Z" fill="#fff"/></svg>(Fav)
  </div>
  <div class="abs top-mail">
    <span class="top-circle"><svg width="18" height="14" viewBox="0 0 18 14"><rect x="1" y="1" width="16" height="12" rx="2" fill="none" stroke="#0a82c9" stroke-width="2"/><path d="M2 3l7 5 7-5" fill="none" stroke="#0a82c9" stroke-width="2"/></svg></span>
    sales@motorharbordepot.example
  </div>
  <div class="abs top-phone">
    <span class="top-circle"><svg width="20" height="20" viewBox="0 0 24 24"><path d="M6.6 10.8a15 15 0 0 0 6.6 6.6l2.2-2.2a1 1 0 0 1 1-.25 11.4 11.4 0 0 0 3.6.57 1 1 0 0 1 1 1V20a1 1 0 0 1-1 1A17 17 0 0 1 3 4a1 1 0 0 1 1-1h3.5a1 1 0 0 1 1 1c0 1.25.2 2.45.57 3.57a1 1 0 0 1-.25 1Z" fill="#0a82c9"/></svg></span>
    (555) 014-2277
  </div>
  <nav class="abs main-nav">
    <a class="active" href="#">HOME</a><a href="#">ABOUT US</a><a href="#">INVENTORY</a><a href="#">FINANCE</a><a href="#">CONTACT</a>
  </nav>
  <a class="abs btn sign-in" href="#">SIGN IN
    <svg width="16" height="14" viewBox="0 0 16 14"><path d="M1 7h9M7 3l4 4-4 4" fill="none" stroke="#fff" stroke-width="2.4"/><path d="M11 1h4v12h-4" fill="none" stroke="#fff" stroke-width="2"/></svg></a>
</header>

<section>
  <div class="abs hero" role="img" aria-label="Red sports coupe driving fast along a wooded road"></div>
  <div class="abs hero-car" role="img" aria-label="Red convertible coupe front view"></div>
  <div class="abs hero-copy">
    <h1>MOTOR HARBOR DEPOT</h1>
    <p>Lorem ipsum dolor sit amet, consectetur adipiscing elit, sed do eiusmod tempor incididunt ut labore et dolore.</p>
    <a class="btn" href="#">GET STARTED
      <svg width="16" height="16" viewBox="0 0 16 16"><circle cx="8" cy="8" r="8" fill="#fff"/><path d="M5 8h5M8 5l3 3-3 3" fill="none" stroke="#0a82c9" stroke-width="2"/></svg></a>
  </div>
  <div class="abs dots"><span></span><span></span><span class="on"></span><span></span><span></span></div>
  <div class="abs side-tools">
    <span><svg width="20" height="20" viewBox="0 0 24 24"><path d="M6.6 10.8a15 15 0 0 0 6.6 6.6l2.2-2.2a1 1 0 0 1 1-.25 11.4 11.4 0 0 0 3.6.57 1 1 0 0 1 1 1V20a1 1 0 0 1-1 1A17 17 0 0 1 3 4a1 1 0 0 1 1-1h3.5a1 1 0 0 1 1 1c0 1.25.2 2.45.57 3.57a1 1 0 0 1-.25 1Z" fill="#0a82c9"/></svg></span>
    <span><svg width="22" height="16" viewBox="0 0 18 14"><rect x="1" y="1" width="16" height="12" rx="1" fill="none" stroke="#0a82c9" stroke-width="1.6"/><path d="M2 2l7 6 7-6" fill="none" stroke="#0a82c9" stroke-width="1.6"/></svg></span>
    <span><svg width="26" height="12" viewBox="0 0 26 12"><path d="M2 9V7l4-1 4-4h7l5 4 2 1v2Z" fill="none" stroke="#0a82c9" stroke-width="1.3"/><circle cx="7" cy="9.5" r="1.8" fill="#fff" stroke="#0a82c9"/><circle cx="19" cy="9.5" r="1.8" fill="#fff" stroke="#0a82c9"/></svg></span>
  </div>
</section>

<section>
  <div class="abs search-band" role="img" aria-label="Blurred blue road scene behind the search bar"></div>
  <form class="abs search-form">
    <div class="select" style="width:146px">Year <svg width="12" height="8" viewBox="0 0 12 8"><path d="M1 1l5 5 5-5" fill="none" stroke="#555" stroke-width="1.6"/></svg></div>
    <div class="select" style="width:146px">Make <svg width="12" height="8" viewBox="0 0 12 8"><path d="M1 1l5 5 5-5" fill="none" stroke="#555" stroke-width="1.6"/></svg></div>
    <div class="select" style="width:146px">Model <svg width="12" height="8" viewBox="0 0 12 8"><path d="M1 1l5 5 5-5" fill="none" stroke="#555" stroke-width="1.6"/></svg></div>
    <div class="select" style="width:146px">Mileage <svg width="12" height="8" viewBox="0 0 12 8"><path d="M1 1l5 5 5-5" fill="none" stroke="#555" stroke-width="1.6"/></svg></div>
    <div class="select" style="width:245px">Color and Drivetrain <svg width="12" height="8" viewBox="0 0 12 8"><path d="M1 1l5 5 5-5" fill="none" stroke="#555" stroke-width="1.6"/></svg></div>
    <a class="btn search-btn" href="#">SEARCH
      <svg width="18" height="18" viewBox="0 0 18 18"><circle cx="7.5" cy="7.5" r="5.5" fill="none" stroke="#fff" stroke-width="2.4"/><path d="M11.5 11.5l5 5" stroke="#fff" stroke-width="2.6"/></svg></a>
  </form>
</section>

<section>
  <div class="abs makes"></div>
  <div class="abs makes-list">
    <span>Velor</span><span>Zent</span><span>Marivel</span><span>Tovan</span><span>Dunharrow</span><span>Pelgrave</span><span>Brant</span><span>Holm</span><span>Kespa</span><span>Oravik</span><span>Pelican</span>
  </div>
  <div class="abs makes-more"><svg width="14" height="9" viewBox="0 0 12 8"><path d="M1 1l5 5 5-5" fill="none" stroke="#222" stroke-width="1.8"/></svg></div>
</section>

<section>
  <div class="abs tabs"><span class="active">ALL</span><span>AWD</span><span>FWD</span></div>

  <div class="abs grid">
    <article class="card">
      <div class="photo p1" role="img" aria-label="Dark brown SUV parked on a city street"></div>
      <span class="badge">AWD</span>
      <h3>2006 Holm Rally ZX4 SE 4DR Sedan Rally</h3>
      <div class="price">$ 1990</div>
      <div class="meta"><span><svg width="13" height="13" viewBox="0 0 13 13"><rect x="1" y="2" width="11" height="10" fill="none" stroke="#0a82c9" stroke-width="1.5"/><path d="M1 5h11" stroke="#0a82c9" stroke-width="1.5"/></svg>2019</span><span><svg width="14" height="12" viewBox="0 0 16 14"><path d="M8 13 1.3 6.7A3.8 3.8 0 0 1 8 2a3.8 3.8 0 0 1 6.7 4.7Z" fill="none" stroke="#0a82c9" stroke-width="1.6"/></svg>4125</span><span><svg width="15" height="12" viewBox="0 0 15 12"><path d="M1 11c1-5 5-7 9-7V1l4 4.5L10 10V7c-4 0-7 1-9 4Z" fill="#0a82c9"/></svg>1,000</span></div>
      <div class="tel"><svg width="13" height="13" viewBox="0 0 24 24"><path d="M6.6 10.8a15 15 0 0 0 6.6 6.6l2.2-2.2a1 1 0 0 1 1-.25 11.4 11.4 0 0 0 3.6.57 1 1 0 0 1 1 1V20a1 1 0 0 1-1 1A17 17 0 0 1 3 4a1 1 0 0 1 1-1h3.5a1 1 0 0 1 1 1c0 1.25.2 2.45.57 3.57a1 1 0 0 1-.25 1Z" fill="#0a82c9"/></svg>555 010 8889</div>
    </article>
    <article class="card">
      <div class="photo p2" role="img" aria-label="Red sports car parked among palm trees"></div>
      <span class="badge">FWD</span>
      <h3>2012 Norda N60 T5 4DR Sedan N60</h3>
      <div class="price">$9 990</div>
      <div class="meta"><span><svg width="13" height="13" viewBox="0 0 13 13"><rect x="1" y="2" width="11" height="10" fill="none" stroke="#0a82c9" stroke-width="1.5"/><path d="M1 5h11" stroke="#0a82c9" stroke-width="1.5"/></svg>2019</span><span><svg width="14" height="12" viewBox="0 0 16 14"><path d="M8 13 1.3 6.7A3.8 3.8 0 0 1 8 2a3.8 3.8 0 0 1 6.7 4.7Z" fill="none" stroke="#0a82c9" stroke-width="1.6"/></svg>4125</span><span><svg width="15" height="12" viewBox="0 0 15 12"><path d="M1 11c1-5 5-7 9-7V1l4 4.5L10 10V7c-4 0-7 1-9 4Z" fill="#0a82c9"/></svg>1,000</span></div>
      <div class="tel"><svg width="13" height="13" viewBox="0 0 24 24"><path d="M6.6 10.8a15 15 0 0 0 6.6 6.6l2.2-2.2a1 1 0 0 1 1-.25 11.4 11.4 0 0 0 3.6.57 1 1 0 0 1 1 1V20a1 1 0 0 1-1 1A17 17 0 0 1 3 4a1 1 0 0 1 1-1h3.5a1 1 0 0 1 1 1c0 1.25.2 2.45.57 3.57a1 1 0 0 1-.25 1Z" fill="#0a82c9"/></svg>555 010 8889</div>
    </article>
    <article class="card">
      <div class="photo p3" role="img" aria-label="Light blue grand touring coupe outside a hotel"></div>
      <span class="badge">AWD</span>
      <h3>2013 Dunharrow Stonecrest 1500 LS</h3>
      <div class="price">$13 990</div>
      <div class="meta"><span><svg width="13" height="13" viewBox="0 0 13 13"><rect x="1" y="2" width="11" height="10" fill="none" stroke="#0a82c9" stroke-width="1.5"/><path d="M1 5h11" stroke="#0a82c9" stroke-width="1.5"/></svg>2019</span><span><svg width="14" height="12" viewBox="0 0 16 14"><path d="M8 13 1.3 6.7A3.8 3.8 0 0 1 8 2a3.8 3.8 0 0 1 6.7 4.7Z" fill="none" stroke="#0a82c9" stroke-width="1.6"/></svg>4125</span><span><svg width="15" height="12" viewBox="0 0 15 12"><path d="M1 11c1-5 5-7 9-7V1l4 4.5L10 10V7c-4 0-7 1-9 4Z" fill="#0a82c9"/></svg>1,000</span></div>
      <div class="tel"><svg width="13" height="13" viewBox="0 0 24 24"><path d="M6.6 10.8a15 15 0 0 0 6.6 6.6l2.2-2.2a1 1 0 0 1 1-.25 11.4 11.4 0 0 0 3.6.57 1 1 0 0 1 1 1V20a1 1 0 0 1-1 1A17 17 0 0 1 3 4a1 1 0 0 1 1-1h3.5a1 1 0 0 1 1 1c0 1.25.2 2.45.57 3.57a1 1 0 0 1-.25 1Z" fill="#0a82c9"/></svg>555 010 8889</div>
    </article>

    <article class="card">
      <div class="photo p4" role="img" aria-label="Yellow supercar parked under autumn trees"></div>
      <span class="badge">AWD</span>
      <h3>2006 Holm Rally ZX4 SE 4DR Sedan Rally</h3>
      <div class="price">$ 1990</div>
      <div class="meta"><span><svg width="13" height="13" viewBox="0 0 13 13"><rect x="1" y="2" width="11" height="10" fill="none" stroke="#0a82c9" stroke-width="1.5"/><path d="M1 5h11" stroke="#0a82c9" stroke-width="1.5"/></svg>2019</span><span><svg width="14" height="12" viewBox="0 0 16 14"><path d="M8 13 1.3 6.7A3.8 3.8 0 0 1 8 2a3.8 3.8 0 0 1 6.7 4.7Z" fill="none" stroke="#0a82c9" stroke-width="1.6"/></svg>4125</span><span><svg width="15" height="12" viewBox="0 0 15 12"><path d="M1 11c1-5 5-7 9-7V1l4 4.5L10 10V7c-4 0-7 1-9 4Z" fill="#0a82c9"/></svg>1,000</span></div>
      <div class="tel"><svg width="13" height="13" viewBox="0 0 24 24"><path d="M6.6 10.8a15 15 0 0 0 6.6 6.6l2.2-2.2a1 1 0 0 1 1-.25 11.4 11.4 0 0 0 3.6.57 1 1 0 0 1 1 1V20a1 1 0 0 1-1 1A17 17 0 0 1 3 4a1 1 0 0 1 1-1h3.5a1 1 0 0 1 1 1c0 1.25.2 2.45.57 3.57a1 1 0 0 1-.25 1Z" fill="#0a82c9"/></svg>555 010 8889</div>
    </article>
    <article class="card featured">
      <div class="photo p5" role="img" aria-label="Red sports car in front of a white resort building"></div>
      <span class="badge" style="background:#0a82c9;color:#fff">AWD</span>
      <h3>2012 Norda N60 T5 4DR Sedan N60</h3>
      <div class="price">$9 990</div>
      <div class="meta"><span><svg width="13" height="13" viewBox="0 0 13 13"><rect x="1" y="2" width="11" height="10" fill="none" stroke="#fff" stroke-width="1.5"/><path d="M1 5h11" stroke="#fff" stroke-width="1.5"/></svg>2019</span><span><svg width="14" height="12" viewBox="0 0 16 14"><path d="M8 13 1.3 6.7A3.8 3.8 0 0 1 8 2a3.8 3.8 0 0 1 6.7 4.7Z" fill="none" stroke="#fff" stroke-width="1.6"/></svg>4125</span><span><svg width="15" height="12" viewBox="0 0 15 12"><path d="M1 11c1-5 5-7 9-7V1l4 4.5L10 10V7c-4 0-7 1-9 4Z" fill="#fff"/></svg>1,000</span></div>
      <div class="tel"><svg width="13" height="13" viewBox="0 0 24 24"><path d="M6.6 10.8a15 15 0 0 0 6.6 6.6l2.2-2.2a1 1 0 0 1 1-.25 11.4 11.4 0 0 0 3.6.57 1 1 0 0 1 1 1V20a1 1 0 0 1-1 1A17 17 0 0 1 3 4a1 1 0 0 1 1-1h3.5a1 1 0 0 1 1 1c0 1.25.2 2.45.57 3.57a1 1 0 0 1-.25 1Z" fill="#fff"/></svg>555 010 8889</div>
    </article>
    <article class="card">
      <div class="photo p6" role="img" aria-label="Silver gullwing sports car parked on a street"></div>
      <span class="badge">FWD</span>
      <h3>2013 Dunharrow Stonecrest 1500 LS</h3>
      <div class="price">$13 990</div>
      <div class="meta"><span><svg width="13" height="13" viewBox="0 0 13 13"><rect x="1" y="2" width="11" height="10" fill="none" stroke="#0a82c9" stroke-width="1.5"/><path d="M1 5h11" stroke="#0a82c9" stroke-width="1.5"/></svg>2019</span><span><svg width="14" height="12" viewBox="0 0 16 14"><path d="M8 13 1.3 6.7A3.8 3.8 0 0 1 8 2a3.8 3.8 0 0 1 6.7 4.7Z" fill="none" stroke="#0a82c9" stroke-width="1.6"/></svg>4125</span><span><svg width="15" height="12" viewBox="0 0 15 12"><path d="M1 11c1-5 5-7 9-7V1l4 4.5L10 10V7c-4 0-7 1-9 4Z" fill="#0a82c9"/></svg>1,000</span></div>
      <div class="tel"><svg width="13" height="13" viewBox="0 0 24 24"><path d="M6.6 10.8a15 15 0 0 0 6.6 6.6l2.2-2.2a1 1 0 0 1 1-.25 11.4 11.4 0 0 0 3.6.57 1 1 0 0 1 1 1V20a1 1 0 0 1-1 1A17 17 0 0 1 3 4a1 1 0 0 1 1-1h3.5a1 1 0 0 1 1 1c0 1.25.2 2.45.57 3.57a1 1 0 0 1-.25 1Z" fill="#0a82c9"/></svg>555 010 8889</div>
    </article>
  </div>
</section>

<section>
  <div class="abs why" role="img" aria-label="Faded background of a car in soft grey light"></div>
  <div class="abs why-car" role="img" aria-label="Silver compact SUV, front three-quarter view"></div>
  <div class="abs why-copy">
    <h2>WHY CHOOSE US</h2>
    <p>Sed ut perspiciatis unde omnis iste natus error sit voluptatem accusantium doloremque laudantium, totam rem aperiam, eaque ipsa quae ab illo inventore veritatis et quasi architecto beatae vitae dicta sunt explicabo. Nemo enim ipsam voluptatem quia voluptas sit aspernatur aut odit aut fugit.</p>
    <a class="btn" href="#">CHECK FOR FINANCIAL STATUS
      <svg width="16" height="16" viewBox="0 0 16 16"><circle cx="8" cy="8" r="8" fill="#fff"/><path d="M5 8h5M8 5l3 3-3 3" fill="none" stroke="#0a82c9" stroke-width="2"/></svg></a>
  </div>
</section>

<section>
  <h2 class="abs reviews-title">REVIEWS</h2>
  <div class="abs arrow" style="left:37px"><svg width="10" height="16" viewBox="0 0 10 16"><path d="M8 1 2 8l6 7" fill="none" stroke="#111" stroke-width="2.4"/></svg></div>
  <div class="abs arrow" style="left:1127px"><svg width="10" height="16" viewBox="0 0 10 16"><path d="M2 1l6 7-6 7" fill="none" stroke="#111" stroke-width="2.4"/></svg></div>

  <article class="abs review" style="left:111px">
    <div class="avatar" role="img" aria-label="Customer portrait"></div>
    <span class="quote">”</span>
    <div class="body">
      <div class="stars"><svg width="112" height="18" viewBox="0 0 112 18"><g fill="#f5a623"><path id="st" d="M9 0l2.6 5.6 6.2.7-4.6 4.2 1.3 6.1L9 13.5 3.5 16.6l1.3-6.1L.2 6.3l6.2-.7Z"/><use href="#st" x="23"/><use href="#st" x="46"/><use href="#st" x="69"/><use href="#st" x="92"/></g></svg></div>
      <p>Ut enim ad minima veniam, quis nostrum exercitationem ullam.</p>
      <div class="who"><b>- MERIDEW</b>&nbsp; Businessman , USA</div>
    </div>
  </article>
  <article class="abs review" style="left:607px">
    <div class="avatar" role="img" aria-label="Customer portrait"></div>
    <span class="quote">”</span>
    <div class="body">
      <div class="stars"><svg width="112" height="18" viewBox="0 0 112 18"><g fill="#f5a623"><use href="#st"/><use href="#st" x="23"/><use href="#st" x="46"/><use href="#st" x="69"/><use href="#st" x="92"/></g></svg></div>
      <p>Ut enim ad minima veniam, quis nostrum exercitationem ullam.</p>
      <div class="who"><b>- MERIDEW</b>&nbsp; Businessman , USA</div>
    </div>
  </article>
</section>

<footer>
  <div class="abs site-footer"></div>
  <div class="abs fcol" style="left:111px;color:#fff">
    <h4>QUICK LINKS</h4>
    <ul><li>»<span>Home</span></li><li>»<span>About Us</span></li><li>»<span>Reviews</span></li><li>»<span>Contact Us</span></li><li>»<span>Finance</span></li></ul>
  </div>
  <div class="abs fcol" style="left:326px;color:#fff">
    <h4>QUICK LINKS</h4>
    <ul><li>»<span>FAQ</span></li><li>»<span>Help Service</span></li><li>»<span>Terms Of Use</span></li><li>»<span>Inventory</span></li><li>»<span>Finance</span></li></ul>
  </div>
  <div class="abs fcol" style="left:551px;color:#fff">
    <h4>CONTACT US</h4>
    <div class="contact-row"><span class="ci"><svg width="12" height="16" viewBox="0 0 12 16"><path d="M6 16S0 9.5 0 6a6 6 0 0 1 12 0c0 3.5-6 10-6 10Z" fill="#0a82c9"/><circle cx="6" cy="6" r="2.2" fill="#fff"/></svg></span><span>410 Harbor Point Road,<br>Lakeview, MI 49000</span></div>
    <div class="contact-row"><span class="ci"><svg width="14" height="14" viewBox="0 0 24 24"><path d="M6.6 10.8a15 15 0 0 0 6.6 6.6l2.2-2.2a1 1 0 0 1 1-.25 11.4 11.4 0 0 0 3.6.57 1 1 0 0 1 1 1V20a1 1 0 0 1-1 1A17 17 0 0 1 3 4a1 1 0 0 1 1-1h3.5a1 1 0 0 1 1 1c0 1.25.2 2.45.57 3.57a1 1 0 0 1-.25 1Z" fill="#0a82c9"/></svg></span><span>(555) 014-2277<br>(555) 014-9538</span></div>
    <div class="contact-row"><span class="ci"><svg width="14" height="11" viewBox="0 0 18 14"><rect x="1" y="1" width="16" height="12" rx="2" fill="none" stroke="#0a82c9" stroke-width="2"/><path d="M2 3l7 5 7-5" fill="none" stroke="#0a82c9" stroke-width="2"/></svg></span><span style="padding-top:6px">info@motorharbordepot.example</span></div>
  </div>
  <div class="abs fcol news" style="left:818px;color:#fff">
    <h4>NEWSLETTER</h4>
    <p>At vero eos et accusamus et iusto odio dignissimos ducimus qui blanditiis.</p>
    <div class="email-field"><svg width="14" height="11" viewBox="0 0 18 14"><rect x="1" y="1" width="16" height="12" rx="2" fill="none" stroke="#0a82c9" stroke-width="2"/><path d="M2 3l7 5 7-5" fill="none" stroke="#0a82c9" stroke-width="2"/></svg>Email Address</div>
    <a class="btn" href="#">SUBSCRIBE
      <svg width="16" height="16" viewBox="0 0 16 16"><circle cx="8" cy="8" r="8" fill="#fff"/><path d="M5 8h5M8 5l3 3-3 3" fill="none" stroke="#0a82c9" stroke-width="2"/></svg></a>
  </div>
  <div class="abs footer-rule"></div>
  <div class="abs copyright" style="color:#fff">© 2019 Motor Harbor Depot. All Rights Reserved</div>
  <div class="abs pay-name">paysecure.example</div>
  <div class="abs pay-cards"><span></span><span></span><span></span><span></span></div>
  <div class="abs live-chat" style="color:#fff"><span>LIVE CHAT</span></div>
</footer>

</body>
</html>
```